Record Label Needs Design for CD Case, Booklet, and CD...

We are a christian record label looking to make a difference in this world.

We need 3 files -
The front and back of CD case and the actual CD graphics.

It is entitled

"Larkspan Records and Friends Summer Sampler 2014"

We will give you the artists and songs on the CD.

Please send IDEAS WE ARE OPEN TO ANYTHING!!!

you can find information on our record label at www.larkspanrecords.net or www.facebook.com/larkspanrecords

The 2 artists on the summer sampler are Ferncastle - and Paper Harbor

I have pictures of Ferncastle attached below, and pictures of paper harbor below...

ferncastlepraise.net has their logo
paper harbors logo is attached...

This is a guaranteed payout and Ive had much luck with pixel bazaar. Looking forward to another successful contest.

martin@larkspanrecords.net

Reason: We haven't had any responses yet so we extended this out a few days!

Reason: We need better designs...

Come on guys!  Send in some new designs!  I am not hard to please!  I just updated the color schemes, etc....

Target Market(s)

Christians

Industry/Entity Type

Artists

Colors
d3a5cc
ed9dc4
8768ae

Requirements
Must have
• Positivity
Nice to have
• Doves are nice
Should not have
• Crosses

```html
<!DOCTYPE html>
<html lang="en">
<head>
<meta charset="utf-8">
<title>Larkspan Records and Friends – Summer Sampler 2014</title>
<link rel="stylesheet" href="https://fonts.googleapis.com/css2?family=Great+Vibes&family=Cormorant+Garamond:ital,wght@1,500&display=swap">
<style>
  :root {
    --sky-dark: #3c4f52;
    --sky-mid: #7f9590;
    --sky-light: #b9c6bd;
    --hill-green: #5f9a2c;
    --meadow: #8fbf3a;
    --river: #b9d3cf;
    --sun-top: rgba(246, 214, 200, 0.55);
    --sun-mid: #f4a24a;
    --sun-low: #e8602a;
    --text-white: #ffffff;
    --year-yellow: #eed63c;
  }
  html, body {
    margin: 0;
    padding: 0;
    width: 1200px;
    height: 1200px;
    overflow: hidden;
  }
  .cover {
    position: relative;
    width: 1200px;
    height: 1200px;
    overflow: hidden;
    background: var(--sky-dark);
  }
  .landscape-photo {
    position: absolute;
    inset: 0;
    background:
      linear-gradient(180deg, transparent 48%, rgba(143,191,58,0.9) 60%, var(--hill-green) 80%, #3f6f22 100%),
      linear-gradient(180deg, var(--sky-dark) 0%, var(--sky-mid) 28%, var(--sky-light) 50%, #9fb48a 60%);
  }
  .river-glow {
    position: absolute;
    left: 380px;
    top: 700px;
    width: 500px;
    height: 500px;
    background: radial-gradient(ellipse 40% 60% at 50% 70%, rgba(185,211,207,0.75), transparent 70%);
  }
  .sun-disc {
    position: absolute;
    left: 267px;
    top: 241px;
    width: 560px;
    height: 560px;
    border-radius: 50%;
    background: linear-gradient(180deg, var(--sun-top) 0%, rgba(246,200,170,0.6) 38%, var(--sun-mid) 55%, var(--sun-low) 78%, rgba(232,96,42,0.35) 100%);
  }
  .dove-area {
    position: absolute;
    left: 400px;
    top: 10px;
    width: 420px;
    height: 400px;
    border-radius: 50%;
    background: radial-gradient(ellipse at 50% 45%, rgba(255,255,255,0.8), rgba(255,255,255,0) 65%);
  }
  .label-line {
    position: absolute;
    left: 203px;
    top: 395px;
    margin: 0;
    font-family: "Cormorant Garamond", Georgia, serif;
    font-style: italic;
    font-weight: 500;
    font-size: 44px;
    color: var(--text-white);
    letter-spacing: 0.5px;
  }
  .title {
    position: absolute;
    left: 170px;
    top: 455px;
    margin: 0;
    font-family: "Great Vibes", cursive;
    font-weight: 400;
    font-size: 150px;
    line-height: 1;
    color: var(--text-white);
    white-space: nowrap;
  }
  .year {
    position: absolute;
    right: 180px;
    top: 620px;
    margin: 0;
    font-family: "Great Vibes", cursive;
    font-size: 92px;
    line-height: 1;
    color: var(--year-yellow);
  }
</style>
</head>
<body>
  <main class="cover">
    <div class="landscape-photo" role="img" aria-label="Photograph of a green valley with a winding river under a stormy sky"></div>
    <div class="river-glow" aria-hidden="true"></div>
    <div class="sun-disc" role="img" aria-label="Glowing sunset circle with a mountain and lake inside"></div>
    <div class="dove-area" role="img" aria-label="White dove flying with wings spread"></div>
    <p class="label-line">Larkspan Records and Friends</p>
    <h1 class="title">Summer Sampler</h1>
    <p class="year">2014</p>
  </main>
</body>
</html>
```